Luxury Wine Label for New Startup Winery

We need a wine label for our new winery startup. We have worked with a local designer but do not feel the resulting label / logo have the elevation required to present our brand as a luxury wine. Our winery is called "Halvorsen Cellars" and we are focused on extremely high quality hand crafted artisan and estate wines from the Pacific Northwest.
We would like to see designs that utilize a tree line, or other imagery that represents the "Halvorsen" part of our company name. Another interesting feature could be wood grain.
A logo will be required based on your design so please design with this in mind:
This logo should be consistent with the wine bottle label design, and should be representative of our high end exclusive wine while giving a sense of place (Oregon/ Pacific Northwest.)
I will supply an image of the design we received from our local designer, PLEASE NOTE: in general we do like wood grain and tree line concepts but feel the execution was poorly done.
ATTN: Logo design should be suitable for use on: Bottles (Red wine/rose/white wine), Bussiness cards, vehicle signage, business signage, etc
P.S.:
If you have a design that is not outside the box we are still interested in seeing it.
Label is for a burgundy style bottle with a label height of 3.5 - 4" and a width of 3.5-4"
any label <= 4"x4" and >=3.5"x3.5" will be acceptable:
HOWEVER Width should be greater than or equal to height due to the bottle format
Target Market(s)
Wine enthusiasts with adequate discretionary budgets to afford $100 bottles of wine.
Industry/Entity Type
Wine / Winery
Requirements
Must have
- A sense of luxury, a feel of exclusivity, and a theme consistent with our product and brand name
Nice to have
- Tree line, wood grain or other wood themes. Serif fonts
Should not have
- anything cheesy, off topic, hard to read script fonts or anything that makes the label hard to read from a few feet away or too busy

```html
<!DOCTYPE html>
<html lang="en">
<head>
<meta charset="utf-8">
<title>Halvorsen Cellars – Syrah Label</title>
<link rel="stylesheet" href="https://fonts.googleapis.com/css2?family=Cinzel:wght@400&family=Cormorant+Garamond:wght@500&display=swap">
<style>
  :root {
    --backdrop: #f1f5f7;
    --label-black: #000000;
    --label-sheen: #0b1512;
    --silver: #c9ccce;
    --silver-dim: #7d8184;
    --rule-silver: #8e9295;
    --gold-rule: #a8912e;
    --grain-dark: #1a0c06;
    --grain-mid: #5a2e14;
    --grain-warm: #8a5428;
    --cream: #f3efe6;
  }
  * { margin: 0; padding: 0; box-sizing: border-box; }
  html, body {
    width: 1200px;
    height: 2201px;
    overflow: hidden;
    background: var(--backdrop);
  }
  .canvas {
    position: relative;
    width: 1200px;
    height: 2201px;
    background: var(--backdrop);
  }
  .label {
    position: absolute;
    left: 155px;
    width: 890px;
    overflow: hidden;
  }
  /* Front label: estate name */
  .label--estate {
    top: 480px;
    height: 723px;
    background:
      linear-gradient(90deg, var(--label-black) 0%, var(--label-sheen) 12%, var(--label-black) 24%, var(--label-black) 100%);
  }
  .rule {
    position: absolute;
    left: 0;
    width: 100%;
    height: 2px;
  }
  .rule--silver {
    background: linear-gradient(90deg, var(--silver-dim) 0%, var(--rule-silver) 40%, var(--rule-silver) 80%, rgba(142,146,149,0.2) 100%);
  }
  .label--estate .rule--top { top: 102px; }
  .label--estate .rule--bottom { top: 621px; }

  .estate-name {
    position: absolute;
    left: 0;
    width: 100%;
    text-align: center;
    font-family: "Cinzel", "Trajan Pro", serif;
    font-weight: 400;
    color: var(--silver);
    line-height: 1;
  }
  .estate-name__primary {
    top: 375px;
    font-size: 108px;
    letter-spacing: 1px;
  }
  .estate-name__secondary {
    top: 497px;
    font-size: 66px;
    letter-spacing: 9px;
  }
  .appellation {
    position: absolute;
    top: 660px;
    left: 0;
    width: 100%;
    text-align: center;
    font-family: "Cormorant Garamond", "Times New Roman", serif;
    font-weight: 500;
    font-size: 26px;
    letter-spacing: 5px;
    color: var(--silver);
  }

  /* Varietal label */
  .label--varietal {
    top: 1268px;
    height: 448px;
    background: var(--grain-dark);
  }
  .wood-grain {
    position: absolute;
    inset: 0;
    background:
      radial-gradient(ellipse 60% 80% at 18% 55%, var(--grain-warm) 0%, rgba(90,46,20,0.6) 40%, rgba(26,12,6,0) 75%),
      radial-gradient(ellipse 55% 45% at 62% 20%, rgba(138,84,40,0.8) 0%, rgba(90,46,20,0.4) 45%, rgba(26,12,6,0) 80%),
      linear-gradient(100deg, var(--grain-mid) 0%, #3a1b0b 45%, var(--grain-dark) 80%, #0c0603 100%);
  }
  .rule--gold { background: var(--gold-rule); height: 2px; }
  .label--varietal .rule--top { top: 103px; }
  .label--varietal .rule--bottom { top: 334px; }
  .varietal {
    position: absolute;
    top: 165px;
    left: 0;
    width: 100%;
    text-align: center;
    font-family: "Cinzel", "Trajan Pro", serif;
    font-weight: 400;
    font-size: 96px;
    letter-spacing: 14px;
    color: var(--cream);
    line-height: 1;
  }
</style>
</head>
<body>
  <main class="canvas">
    <section class="label label--estate">
      <div class="rule rule--silver rule--top"></div>
      <div class="estate-name estate-name__primary">HALVORSEN</div>
      <div class="estate-name estate-name__secondary">CELLARS</div>
      <div class="rule rule--silver rule--bottom"></div>
      <div class="appellation">WILLAMETTE VALLEY</div>
    </section>

    <section class="label label--varietal">
      <div class="wood-grain" role="img" aria-label="Dark polished burl wood grain in deep browns and amber"></div>
      <div class="rule rule--gold rule--top"></div>
      <div class="varietal">SYRAH</div>
      <div class="rule rule--gold rule--bottom"></div>
    </section>
  </main>
</body>
</html>
```